Carpal Tunnel - PPC Landing Page

We need to do a SINGLE page landing page for a doctor who specializes in Carpal Tunnel syndrome - please research if you're not familiar - it's very common.

Landing page essentials:
Must have a form in upper right hand corner:
Form title: "Get a free diagnosis."
Form inputs: Name, Phone, Email, Requested Appointment time

Page is for PPC, so needs to be simple and light on content. Content has been provided and attached to this project.

No navigation, just a single page.

Industry/Entity Type

Health

Coding

Coded - Design and coding required

Number of Pages Required

1 page

Requirements
Must have
• Elegant look - Conversion optimized for form and phone
• Responsive design.
Should not have
• Old outdated images.

```html
<!DOCTYPE html>
<html lang="en">
<head>
<meta charset="utf-8">
<title>Dr. Halvern – Carpal Tunnel Specialist</title>
<link href="https://fonts.googleapis.com/css2?family=Open+Sans:wght@400;600;700&family=Roboto+Slab:wght@700&display=swap" rel="stylesheet">
<style>
:root{
  --blue:#1e6fc2;
  --blue-dark:#15549a;
  --red:#c4242b;
  --ink:#3b3f45;
  --muted:#6b7078;
  --grey-bg:#eef1f4;
  --line:#d6dbe1;
  --hero-a:#dfe8f2;
  --hero-b:#f7f9fc;
}
*{box-sizing:border-box;margin:0;padding:0}
html,body{width:1200px;height:2216px;overflow:hidden}
body{font-family:"Open Sans",Arial,sans-serif;color:var(--ink);background:#fff;position:relative}
.hero{position:absolute;left:0;top:0;width:1200px;height:372px;background:linear-gradient(90deg,var(--hero-a),var(--hero-b) 60%,#fff)}
.hero-photo{position:absolute;left:130px;top:0;width:330px;height:372px;background:linear-gradient(180deg,#c9d3dc,#e6ebf0)}
.hero-brand{position:absolute;left:560px;top:250px;width:300px;text-align:center}
.hero-brand h1{font-family:"Roboto Slab",Georgia,serif;font-size:44px;color:var(--blue);line-height:1}
.hero-brand p{font-size:12px;color:var(--muted);margin-top:8px;letter-spacing:.5px}
.form{position:absolute;left:870px;top:0;width:290px;height:352px;background:#fff;padding:22px 24px;box-shadow:0 2px 8px rgba(0,0,0,.12)}
.form h2{font-size:26px;font-weight:600;color:var(--ink);letter-spacing:.5px;margin-bottom:16px}
.form h2 span{color:var(--red)}
.form .field{height:34px;border:1px solid var(--line);margin-bottom:12px;font-size:12px;color:#999;padding:8px 10px}
.form .submit{display:block;width:120px;height:38px;margin:18px 0 0 auto;background:var(--red);color:#fff;font-weight:700;font-size:14px;border:0;letter-spacing:1px}
.about{position:absolute;left:0;top:372px;width:1200px;height:358px}
.about h2{position:absolute;left:60px;top:50px;font-size:38px;font-weight:400;color:var(--muted)}
.about h2 span{color:var(--blue)}
.about .rule{position:absolute;left:60px;top:108px;width:1080px;height:1px;background:var(--line)}
.about-art{position:absolute;left:60px;top:125px;width:330px;height:205px;background:linear-gradient(135deg,#f3d9c8,#cfe0f1)}
.about-text{position:absolute;left:420px;top:135px;width:720px;font-size:14px;line-height:1.6}
.about-text p{margin-bottom:14px}
.conditions{position:absolute;left:0;top:730px;width:1200px;height:720px;background:var(--grey-bg)}
.conditions h2{text-align:center;font-size:28px;font-weight:400;color:var(--muted);margin-top:34px}
.conditions h2 span{color:var(--blue)}
.card{position:absolute;background:#fff;padding:18px 22px;border:1px solid var(--line)}
.card h3{display:flex;align-items:center;font-size:17px;font-weight:600;color:var(--blue);margin-bottom:10px}
.card h3 b{width:28px;height:28px;border-radius:50%;background:var(--blue);color:#fff;font-size:14px;display:flex;align-items:center;justify-content:center;margin-right:10px}
.card p{font-size:12px;line-height:1.6;color:var(--muted)}
.c1{left:60px;top:90px;width:530px;height:200px}
.c2{left:610px;top:90px;width:530px;height:200px}
.c3{left:60px;top:305px;width:530px;height:200px}
.c4{left:610px;top:305px;width:530px;height:200px}
.c5{left:60px;top:520px;width:1080px;height:170px}
.reviews{position:absolute;left:0;top:1450px;width:1200px;height:730px}
.reviews h2{text-align:center;font-size:30px;font-weight:700;color:var(--ink);margin-top:24px;letter-spacing:.5px}
.reviews h2 span{color:var(--blue)}
.review{position:absolute;top:120px;width:300px;text-align:center}
.review .avatar{width:200px;height:200px;border-radius:50%;margin:0 auto;background:linear-gradient(180deg,#b9c4cf,#dde3e9);border:6px solid var(--grey-bg)}
.review blockquote{font-size:18px;font-weight:600;line-height:1.5;margin-top:50px;color:var(--ink)}
.review cite{display:block;font-style:normal;font-size:13px;color:var(--muted);margin-top:22px}
.review cite b{color:var(--blue)}
.r1{left:90px}.r2{left:450px}.r3{left:810px}
.footer{position:absolute;left:0;top:2180px;width:1200px;height:36px;background:var(--blue);color:#fff;font-size:11px;text-align:center;line-height:36px}
</style>
</head>
<body>
<header class="hero">
  <div class="hero-photo" role="img" aria-label="Portrait of the doctor in a white coat"></div>
  <div class="hero-brand">
    <h1>Dr. Halvern</h1>
    <p>specialist in Carpal Tunnel Syndrome</p>
  </div>
  <form class="form">
    <h2>GET A <span>FREE</span> DIAGNOSIS</h2>
    <div class="field">Name</div>
    <div class="field">Phone</div>
    <div class="field">Email</div>
    <div class="field">Requested Appointment time</div>
    <button class="submit" type="button">SUBMIT</button>
  </form>
</header>

<section class="about">
  <h2>What is <span>Carpal Tunnel Syndrome</span></h2>
  <div class="rule"></div>
  <div class="about-art" role="img" aria-label="Illustration of the hand and wrist showing the median nerve"></div>
  <div class="about-text">
    <p>In Dr. Halvern's clinical practice, Carpal Tunnel Syndrome is one of the most commonly reported health problems. Carpal tunnel occurs when swelling pinches the median nerve, which provides sensation to the palm side of the thumb, index finger, middle finger and the inside half of the ring finger.</p>
    <p>The result can be a combination of tingling, numbness, weakness and pain in the fingers, thumb, palm or the forearm. If the condition is not treated, permanent deterioration of muscle tissue can occur.</p>
  </div>
</section>

<section class="conditions">
  <h2>Other conditions treated by <span>Dr. Halvern:</span></h2>
  <article class="card c1">
    <h3><b>1</b>Cubital Tunnel Syndrome (Cell Phone Elbow)</h3>
    <p>Similar to carpal tunnel syndrome, cubital tunnel syndrome is a condition brought on by increased pressure. This occurs when there is increased pressure on the ulnar nerve at the elbow. The ulnar nerve runs through a tunnel of tissue near the inside of the elbow and controls sensation in the ring and little fingers. Long periods with the elbow bent, such as holding a phone, can worsen it.</p>
  </article>
  <article class="card c2">
    <h3><b>2</b>DeQuervains Tenosynovitis</h3>
    <p>Also known as first dorsal compartment tendonitis, this is a painful condition that affects the tendons on the thumb side of the wrist. Swelling of the sheath around these tendons causes pain with gripping, pinching, twisting or lifting. It often follows repetitive hand use and is common in new parents who lift infants many times a day.</p>
  </article>
  <article class="card c3">
    <h3><b>3</b>Dupuytren's Disease</h3>
    <p>Dupuytren's disease is caused by an abnormal thickening of the tissue beneath the skin of the palm and fingers. Cords and nodules slowly form and can pull one or more fingers toward the palm so they no longer straighten fully. The ring and little fingers are most often affected, and early care helps keep the hand working well.</p>
  </article>
  <article class="card c4">
    <h3><b>4</b>Hand Sprains</h3>
    <p>Sprains result from forcing a joint to perform a function against its normal range of motion. Finger sprains occur when the ligaments which are attached to the bones are overstretched and the result is pain, swelling and difficulty moving the finger. Prompt assessment and splinting help the ligament heal and restore strength and flexibility.</p>
  </article>
  <article class="card c5">
    <h3><b>5</b>Hand Fractures</h3>
    <p>Fractures of the fingers occur when the finger or hand hits a solid object with force. Fractures are most common at the base of the little finger, often called a boxer's fracture. Injuries can also happen in falls, sports or accidents at work. A correct diagnosis is important because a poorly healed break may leave the hand stiff or crooked. Treatment ranges from splints and casts to minor surgery, depending on the type of break, followed by exercises that bring back grip and motion.</p>
  </article>
</section>

<section class="reviews">
  <h2>WHAT OUR <span>PATIENT</span> SAY ABOUT ME</h2>
  <figure class="review r1">
    <div class="avatar" role="img" aria-label="Patient photo"></div>
    <blockquote>“ It is a long established fact that a reader will be distracted by the readable content layout ”</blockquote>
    <cite><b>Sam Porter</b>, Creative Director</cite>
  </figure>
  <figure class="review r2">
    <div class="avatar" role="img" aria-label="Patient photo"></div>
    <blockquote>“ It is a long established fact that a reader will be distracted by the readable content layout ”</blockquote>
    <cite><b>Sam Porter</b>, Creative Director</cite>
  </figure>
  <figure class="review r3">
    <div class="avatar" role="img" aria-label="Patient photo"></div>
    <blockquote>“ It is a long established fact that a reader will be distracted by the readable content layout ”</blockquote>
    <cite><b>Sam Porter</b>, Creative Director</cite>
  </figure>
</section>

<footer class="footer">© 2016 Dr. Halvern. All Rights Reserved.</footer>
</body>
</html>
```